Responsive OnePage Design for recruitment company

BrightCrew is a modern company that sources interim people for its customers. Mostly developers, scrum master, project managers and designers. In this website we want to tell something about us, about how we work, our customers and we want our candidates be able to subscribe. The subscription form should be several fields (name, surname, email address, phone number and the possibility to upload your resume.We want it to fit into a existing wordpress plugin. We also want a listing of our job opportunities. The listing should be designed in a clear readable overview and if you click on the job you should get the details and be able to respond quickly by filling in you name, surname, email address, rate, phone number and upload your resume. We want this to be a standard configurable plugin. It should be easy to fill in the jobs in Wordpress by our administrator. We want a fresh, modern and cool design. It should be a responsive onepage design. If you click on a listed job you should stay on the same page. Our logo is added.

Target Market(s)

recruitment

Industry/Entity Type

Recruitment

Font styles to use
Sans Serif

Colors

Designer to choose colors to be used in the design.

Requirements
Must have
• Onepage design
• listing of job opportunities
• subscription forms
• be responsive

```html
<!DOCTYPE html>
<html lang="en">
<head>
<meta charset="utf-8">
<title>BrightCrew – Recruitment One Page</title>
<link rel="stylesheet" href="https://fonts.googleapis.com/css2?family=Montserrat:wght@600;700&family=Open+Sans:ital,wght@0,400;0,600;0,700;1,400&display=swap">
<style>
:root{
  --navy:#1f2b44;
  --blue:#1656c4;
  --blue-dark:#0f44a3;
  --orange:#f7931e;
  --peach:#f8dcc6;
  --lavender:#eceefb;
  --grey-text:#8a8f99;
  --grey-bg:#efefef;
  --dark:#232323;
  --footer:#29323d;
  --white:#ffffff;
}
*{box-sizing:border-box;margin:0;padding:0}
html,body{width:1200px;height:1200px;overflow:hidden;background:var(--white)}
body{font-family:"Open Sans",Arial,sans-serif;color:var(--navy)}
.stage{position:absolute;left:0;top:0;width:1500px;height:1500px;transform:scale(.8);transform-origin:0 0}
.page{position:absolute;left:557px;top:15px;width:325px;height:1473px;background:var(--white)}
.abs{position:absolute}
.center{text-align:center;left:0;right:0}
.section-title{font-weight:700;font-size:8px;letter-spacing:.2px;color:var(--navy)}
.section-text{font-size:4px;line-height:8px;color:var(--grey-text)}
.btn-orange{background:var(--orange);color:var(--white);font-weight:700;font-size:4.5px;border-radius:9px;display:flex;align-items:center;justify-content:center;gap:2px}

/* nav */
.brand{font-family:"Open Sans",sans-serif;font-weight:600;font-size:8px;letter-spacing:1.6px;color:var(--navy)}
.nav{display:flex;gap:8px;font-size:4.5px;color:var(--navy);align-items:center}
.nav .active{color:var(--blue)}
.nav .signup{color:var(--blue)}
.nav .login{background:var(--blue);color:var(--white);border-radius:5px;padding:1.5px 7px}

/* hero */
.hero{left:0;top:19px;width:325px;height:161px;overflow:hidden;background:linear-gradient(180deg,var(--peach) 0%,#fbeee3 60%,#fff 100%)}
.hero h1{font-family:"Montserrat",sans-serif;font-weight:700;font-size:10.5px;line-height:13px;color:var(--navy)}
.hero p{font-size:4.6px;line-height:9px;color:#6c6a6a}
.photo{background:linear-gradient(160deg,#d9c8bb,#8e7b6c)}

/* cards */
.card{position:absolute;width:74px;height:95px;background:var(--blue);box-shadow:0 2px 4px rgba(20,60,150,.3);color:var(--white);text-align:center}
.card svg{display:block;margin:17px auto 0}
.card h3{font-size:4.4px;font-weight:700;margin-top:4px}
.card p{font-size:3.4px;line-height:6px;margin:2px 8px 0}

/* process */
.process{left:0;top:708px;width:325px;height:182px;background:var(--dark);overflow:hidden}
.step{position:absolute;left:33px;width:65px;height:13px;border-radius:7px;background:var(--blue);color:var(--white);font-size:4px;font-weight:600;display:flex;align-items:center;gap:3px;padding-left:3px}
.step b{width:9px;height:9px;border:.8px solid var(--white);border-radius:50%;display:flex;align-items:center;justify-content:center;font-size:4px}
.form-head{left:219px;top:60px;width:87px;height:21px;background:var(--blue);color:var(--white);font-weight:700;font-size:8px;display:flex;align-items:center;justify-content:center}
.field{position:absolute;left:226px;width:72px;height:14px;border:.8px solid #bbb;background:rgba(0,0,0,.55);color:#ddd;font-size:4.5px;padding-left:4px;display:flex;align-items:center}
.submit{position:absolute;left:226px;top:162px;width:72px;height:14px;background:var(--orange);color:var(--white);font-size:4.5px;font-weight:700;display:flex;align-items:center;justify-content:center}

/* testimonials */
.arrow-circle{position:absolute;width:14px;height:14px;border:.8px solid #999;border-radius:50%;display:flex;align-items:center;justify-content:center}
.person{position:absolute;width:80px;text-align:center}
.avatar{width:29px;height:29px;border-radius:50%;margin:0 auto;background:linear-gradient(160deg,#e9dac9,#b8977c);border:1px solid #ddd}
.person h4{font-size:4.5px;color:var(--blue);font-weight:700;margin-top:7px}
.person small{display:block;font-size:3.6px;color:var(--grey-text);line-height:6px}
.person p{font-size:3.8px;line-height:8px;color:var(--grey-text);font-style:italic;margin-top:1px}

/* blog */
.blog{left:0;top:1023px;width:325px;height:162px;background:var(--grey-bg)}
.post{position:absolute;top:52px;width:75px}
.post .thumb{height:56px;border:2px solid var(--white);box-shadow:0 1px 2px rgba(0,0,0,.2)}
.post h4{font-size:4.5px;line-height:7.5px;color:var(--blue);font-weight:700;margin-top:5px}
.post small{display:block;font-size:3.8px;color:var(--grey-text);line-height:7px}
.post a{font-size:3.6px;color:var(--orange);font-weight:700;text-decoration:underline}

/* jobs */
.job-box{left:35px;top:1229px;width:254px;height:139px;border:1.5px solid #e1e1e1;border-radius:10px;background:var(--white)}
.job{position:absolute;left:12px;width:230px;height:21px;border-radius:10px;background:var(--white);box-shadow:0 0 3px rgba(0,0,0,.15);display:flex;align-items:center;overflow:hidden}
.job .num{width:12px;height:12px;border-radius:50%;background:var(--blue);color:var(--white);font-size:6px;font-weight:700;display:flex;align-items:center;justify-content:center;margin-left:10px}
.job .title{font-size:5px;font-weight:700;color:var(--navy);margin-left:6px;flex:1}
.job .apply{width:58px;height:100%;background:var(--orange);color:var(--white);font-weight:700;font-size:8px;letter-spacing:.6px;display:flex;align-items:center;justify-content:center;gap:2px;border-radius:0 10px 10px 0}
.job .apply i{width:6px;height:6px;border-radius:50%;background:var(--white);display:inline-flex;align-items:center;justify-content:center}

/* footer */
.footer{left:0;top:1382px;width:325px;height:91px;background:var(--footer);color:#c8ccd2}
.footer .brand{color:var(--white);font-size:7px}
.footer h5{font-size:3.8px;font-weight:700;color:var(--white);text-decoration:underline;margin-bottom:3px}
.footer li{list-style:none;font-size:3.6px;line-height:7px}
.footer p{font-size:3.6px;line-height:7px}
.dot{display:inline-block;width:7px;height:7px;border-radius:50%;background:#c8ccd2;margin-right:2px}
</style>
</head>
<body>
<div class="stage">
<div class="page">

  <!-- header -->
  <div class="abs brand" style="left:26px;top:1px">BRIGHTCREW</div>
  <nav class="abs nav" style="left:121px;top:2px">
    <span class="active">Home</span><span>About us</span><span>Members</span><span>Joblist</span><span>Contact us</span><span class="signup">Sign up</span><span class="login">Log in</span>
  </nav>

  <!-- hero -->
  <section class="abs hero">
    <div class="abs photo" style="left:183px;top:6px;width:142px;height:150px;border-radius:40px 0 0 0" role="img" aria-label="Photo of a cheerful young woman sitting cross-legged with a laptop, coffee mug beside her"></div>
    <h1 class="abs" style="left:35px;top:37px">READY FOR GETTING<br>GOOD JOB</h1>
    <p class="abs" style="left:35px;top:64px">Lorem ipsum is simply dummy text of the printing<br>and typesetting industry.</p>
    <div class="abs btn-orange" style="left:35px;top:90px;width:59px;height:16px">
      <svg width="6" height="6" viewBox="0 0 24 24" fill="none" stroke="#fff" stroke-width="2.5"><path d="M22 16.9v3a2 2 0 0 1-2.2 2A19.8 19.8 0 0 1 2.1 4.2 2 2 0 0 1 4.1 2h3a2 2 0 0 1 2 1.7c.1 1 .4 1.9.7 2.8a2 2 0 0 1-.5 2.1L8 9.9a16 16 0 0 0 6 6l1.3-1.3a2 2 0 0 1 2.1-.5c.9.3 1.8.6 2.8.7a2 2 0 0 1 1.8 2z"/></svg>HIRE JOB</div>
    <svg class="abs" style="left:0;top:120px" width="325" height="42" viewBox="0 0 325 42" preserveAspectRatio="none"><path d="M0 30 C60 20 100 50 160 40 C220 30 260 0 325 25 L325 42 L0 42Z" fill="#fff"/></svg>
  </section>

  <!-- about -->
  <h2 class="abs center section-title" style="top:201px">ABOUT BRIGHTCREW</h2>
  <p class="abs center section-text" style="top:218px">It is a long established fact that a reader will be distracted by the readable content of a page<br>when looking at its layout. The point of using Lorem Ipsum is that it has a more-or-less<br>normal distribution of letters use it now demo purpose.</p>
  <div class="abs" style="left:81px;top:255px;width:155px;height:116px;background:#e6e6e6;border-radius:3px"></div>
  <div class="abs" style="left:87px;top:262px;width:143px;height:103px;background:linear-gradient(135deg,#f7b45c,#f19a3e)" role="img" aria-label="Illustration of two support staff working at desks with headsets, with a video play button"></div>
  <svg class="abs" style="left:154px;top:309px" width="14" height="14" viewBox="0 0 14 14"><circle cx="7" cy="7" r="7" fill="#e53935"/><path d="M5.5 4 L10 7 L5.5 10Z" fill="#fff"/></svg>

  <!-- why choose us -->
  <svg class="abs" style="left:0;top:418px" width="325" height="283" viewBox="0 0 325 283"><path d="M0 0 L160 40 L325 58 L325 170 C240 240 120 275 0 283Z" fill="var(--lavender)"/></svg>
  <h2 class="abs center section-title" style="top:392px">WHY CHOOSE US</h2>
  <p class="abs center section-text" style="top:409px">It is a long established fact that a reader will be distracted by the readable content of a page<br>when looking at its layout letters use it now demo purpose.</p>
  <div class="abs btn-orange" style="left:123px;top:437px;width:79px;height:17px">
    <svg width="6" height="6" viewBox="0 0 24 24" fill="none" stroke="#fff" stroke-width="2.5"><path d="M22 16.9v3a2 2 0 0 1-2.2 2A19.8 19.8 0 0 1 2.1 4.2 2 2 0 0 1 4.1 2h3a2 2 0 0 1 2 1.7c.1 1 .4 1.9.7 2.8a2 2 0 0 1-.5 2.1L8 9.9a16 16 0 0 0 6 6l1.3-1.3a2 2 0 0 1 2.1-.5c.9.3 1.8.6 2.8.7a2 2 0 0 1 1.8 2z"/></svg>HIRE JOB</div>

  <div class="card" style="left:46px;top:472px">
    <svg width="22" height="20" viewBox="0 0 24 22" fill="none" stroke="#fff" stroke-width="1.2"><path d="M12 20 C2 13 1 8 3 5 C5 2 9 2 12 6 C15 2 19 2 21 5 C23 8 22 13 12 20Z"/><path d="M7 11 L10 9 L14 12 L17 10"/></svg>
    <h3>GOODWILL</h3><p>It is a long established fact that a reader will be distracted by the readable content page.</p></div>
  <div class="card" style="left:126px;top:472px">
    <svg width="22" height="20" viewBox="0 0 24 24" fill="none" stroke="#fff" stroke-width="1.2"><path d="M12 2a7 7 0 0 0-4 12.7V18h8v-3.3A7 7 0 0 0 12 2z"/><path d="M9 21h6M13 6l-3 5h4l-3 5"/></svg>
    <h3>HASLE FREE</h3><p>It is a long established fact that a reader will be distracted by the readable content page.</p></div>
  <div class="card" style="left:205px;top:472px">
    <svg width="22" height="20" viewBox="0 0 24 24" fill="none" stroke="#fff" stroke-width="1.2"><rect x="6" y="5" width="10" height="16" rx="5"/><path d="M11 5v5M18 3c2 1 3 3 2 5"/></svg>
    <h3>ONLINE APPLY</h3><p>It is a long established fact that a reader will be distracted by the readable content page.</p></div>
  <div class="card" style="left:46px;top:581px">
    <svg width="22" height="20" viewBox="0 0 24 24" fill="none" stroke="#fff" stroke-width="1.2"><path d="M12 2 L20 5 V11 C20 16 16 20 12 22 C8 20 4 16 4 11 V5Z"/><rect x="9" y="11" width="6" height="5"/><path d="M10 11V9a2 2 0 0 1 4 0v2"/></svg>
    <h3>JOB SECURITY</h3><p>It is a long established fact that a reader will be distracted by the readable content page.</p></div>
  <div class="card" style="left:126px;top:581px">
    <svg width="22" height="20" viewBox="0 0 24 24" fill="none" stroke="#fff" stroke-width="1.2"><circle cx="11" cy="10" r="8"/><circle cx="11" cy="10" r="5.5"/><path d="M13 8c-.5-1-3.5-1-3.5.5S13 10 13 11.5 10 13 9 12M11 6v8"/><path d="M16 18l4 3"/></svg>
    <h3>BEST SALARY</h3><p>It is a long established fact that a reader will be distracted by the readable content page.</p></div>
  <div class="card" style="left:205px;top:581px">
    <svg width="22" height="20" viewBox="0 0 24 24" fill="none" stroke="#fff" stroke-width="1.2"><path d="M4 14 L12 4 L16 8 L9 16Z"/><circle cx="16" cy="15" r="3"/><path d="M11 22c0-3 2-4 5-4s5 1 5 4"/></svg>
    <h3>GET INFORMATION</h3><p>It is a long established fact that a reader will be distracted by the readable content page.</p></div>

  <!-- process -->
  <section class="abs process">
    <div class="abs" style="left:80px;top:50px;width:140px;height:132px;background:radial-gradient(ellipse at 55% 45%,#8a6e5c 0%,#4a3a32 45%,#232323 80%)" role="img" aria-label="Photo of a young woman smiling at a laptop with a coffee cup"></div>
    <h2 class="abs center section-title" style="top:21px;color:var(--white)">LOOK AT PROCESS</h2>
    <p class="abs center section-text" style="top:37px;color:#e0e0e0">It is a long established fact that a reader will be distracted by the readable content of a page<br>when looking at its layout use demo text now design purpose.</p>
    <div class="step" style="top:71px"><b>1</b>Put Your Information</div>
    <div class="step" style="top:92px"><b>2</b>Put Phone Number</div>
    <div class="step" style="top:113px"><b>3</b>Put OTP</div>
    <div class="step" style="top:134px"><b>4</b>Submit Now</div>
    <div class="abs form-head">FILL UP FORM</div>
    <div class="field" style="top:86px">Name</div>
    <div class="field" style="top:105px">Ph no</div>
    <div class="field" style="top:124px">Mail id</div>
    <div class="field" style="top:143px;justify-content:space-between;padding-right:4px">Upload your resume<svg width="5" height="4" viewBox="0 0 10 6" fill="none" stroke="#ddd"><path d="M1 1l4 4 4-4"/></svg></div>
    <div class="submit">SUBMIT NOW</div>
  </section>

  <!-- testimonials -->
  <h2 class="abs center section-title" style="top:908px">CLIENTS TESTIMONIALS</h2>
  <p class="abs center section-text" style="top:923px">It is a long established fact that a reader will be distracted by content</p>
  <div class="arrow-circle" style="left:16px;top:967px"><svg width="4" height="6" viewBox="0 0 4 6" fill="none" stroke="#999"><path d="M3 .5L1 3l2 2.5"/></svg></div>
  <div class="arrow-circle" style="left:291px;top:967px"><svg width="4" height="6" viewBox="0 0 4 6" fill="none" stroke="#999"><path d="M1 .5L3 3 1 5.5"/></svg></div>
  <div class="person" style="left:33px;top:941px"><div class="avatar" role="img" aria-label="Client portrait"></div><h4>SAM PORTER</h4><small>United States</small><p>It is a long established fact that a<br>reader will use content page.</p></div>
  <div class="person" style="left:119px;top:941px"><div class="avatar" role="img" aria-label="Client portrait"></div><h4>LINA VALE</h4><small>Colombia</small><p>It is a long established fact that a<br>reader will use content page.</p></div>
  <div class="person" style="left:204px;top:941px"><div class="avatar" style="background:linear-gradient(160deg,#d6c2b0,#5a4336)" role="img" aria-label="Client portrait"></div><h4>MARCO DENE</h4><small>Melbourne</small><p>It is a long established fact that a<br>reader will use content page.</p></div>

  <!-- blog -->
  <section class="abs blog">
    <h2 class="abs center section-title" style="top:16px">LATEST BLOG</h2>
    <p class="abs center section-text" style="top:30px">long established fact that a reader will be distracted by content</p>
    <div class="arrow-circle" style="left:19px;top:76px;width:12px;height:12px"><svg width="4" height="6" viewBox="0 0 4 6" fill="none" stroke="#999"><path d="M3 .5L1 3l2 2.5"/></svg></div>
    <div class="arrow-circle" style="left:289px;top:76px;width:12px;height:12px"><svg width="4" height="6" viewBox="0 0 4 6" fill="none" stroke="#999"><path d="M1 .5L3 3 1 5.5"/></svg></div>
    <article class="post" style="left:37px"><div class="thumb" style="background:linear-gradient(180deg,#f4f4f4,#cfc7bf)" role="img" aria-label="Photo of a cheerful woman with a laptop"></div><h4>Lorem Ipsum is simply dummy<br>text of the industry.</h4><small>5 hours continious class...</small><a>LEARN MORE&gt;&gt;</a></article>
    <article class="post" style="left:124px"><div class="thumb" style="background:linear-gradient(135deg,#b98b6a,#e8d3bb)" role="img" aria-label="Photo of a woman reading in a café"></div><h4>Lorem Ipsum is simply dummy<br>text of the industry.</h4><small>5 hours continious class...</small><a>LEARN MORE&gt;&gt;</a></article>
    <article class="post" style="left:210px"><div class="thumb" style="background:linear-gradient(135deg,#8d8f96,#d7d9dd)" role="img" aria-label="Photo of colleagues talking in an office meeting"></div><h4>Lorem Ipsum is simply dummy<br>text of the industry.</h4><small>5 hours continious class...</small><a>LEARN MORE&gt;&gt;</a></article>
  </section>

  <!-- job list -->
  <h2 class="abs center section-title" style="top:1200px">OUR JOB LIST</h2>
  <p class="abs center section-text" style="top:1215px">It is a long established fact that a reader will be distracted by content</p>
  <div class="abs job-box">
    <div class="job" style="top:6px"><span class="num">1</span><span class="title">POST MANAGER DEBSOLUTION OFFICE</span><span class="apply">APPLY <i><svg width="3" height="3" viewBox="0 0 4 6" fill="none" stroke="#f7931e" stroke-width="1.2"><path d="M1 .5L3 3 1 5.5"/></svg></i></span></div>
    <div class="job" style="top:32px"><span class="num">1</span><span class="title">POST MANAGER DEBSOLUTION OFFICE</span><span class="apply">APPLY <i><svg width="3" height="3" viewBox="0 0 4 6" fill="none" stroke="#f7931e" stroke-width="1.2"><path d="M1 .5L3 3 1 5.5"/></svg></i></span></div>
    <div class="job" style="top:58px"><span class="num">1</span><span class="title">POST MANAGER DEBSOLUTION OFFICE</span><span class="apply">APPLY <i><svg width="3" height="3" viewBox="0 0 4 6" fill="none" stroke="#f7931e" stroke-width="1.2"><path d="M1 .5L3 3 1 5.5"/></svg></i></span></div>
    <div class="job" style="top:84px"><span class="num">1</span><span class="title">POST MANAGER DEBSOLUTION OFFICE</span><span class="apply">APPLY <i><svg width="3" height="3" viewBox="0 0 4 6" fill="none" stroke="#f7931e" stroke-width="1.2"><path d="M1 .5L3 3 1 5.5"/></svg></i></span></div>
    <div class="job" style="top:110px"><span class="num">1</span><span class="title">POST MANAGER DEBSOLUTION OFFICE</span><span class="apply">APPLY <i><svg width="3" height="3" viewBox="0 0 4 6" fill="none" stroke="#f7931e" stroke-width="1.2"><path d="M1 .5L3 3 1 5.5"/></svg></i></span></div>
  </div>
  <div class="arrow-circle" style="left:294px;top:1285px;width:12px;height:12px"><svg width="6" height="4" viewBox="0 0 6 4" fill="none" stroke="#999"><path d="M.5 3L3 1l2.5 2"/></svg></div>
  <div class="arrow-circle" style="left:294px;top:1302px;width:12px;height:12px"><svg width="6" height="4" viewBox="0 0 6 4" fill="none" stroke="#999"><path d="M.5 1L3 3l2.5-2"/></svg></div>

  <!-- footer -->
  <footer class="abs footer">
    <div class="abs brand" style="left:37px;top:14px">BRIGHTCREW</div>
    <p class="abs" style="left:36px;top:24px">It is a long established fact that a reader<br>will use content page use this demo text<br>for demo purpose.</p>
    <div class="abs" style="left:124px;top:16px"><h5>SITELINK</h5><ul><li>Home</li><li>About us</li><li>Members</li><li>Joblist</li><li>Contact us</li></ul></div>
    <div class="abs" style="left:164px;top:16px"><h5>WHY CHOOSE US</h5><ul><li>Goodwill</li><li>Salary guarantee</li><li>Hassle free</li></ul></div>
    <div class="abs" style="left:209px;top:16px"><h5>COMPANY RULES</h5><ul><li>Rules &amp; regulations</li><li>Privacy policy</li><li>Terms conditions</li><li>Help</li></ul></div>
    <div class="abs" style="left:260px;top:16px"><h5>CONTACT US</h5>
      <p>&#9742; +100-555-0142<br>&#9993; hello@brightcrew.example</p>
      <div style="margin-top:2px;margin-left:2px"><span class="dot"></span><span class="dot"></span><span class="dot"></span></div>
    </div>
    <p class="abs center" style="top:77px;text-align:center;font-size:3.4px">© 2003-2018 website, Inc. All rights reserved.</p>
  </footer>

</div>
</div>
</body>
</html>
```